Business card design needed

www.marlonfab.com.au
Our primary services:
On-site welding.
On-site industrial maintenance.
On-site repairs and capital works projects specialising in pipe fabrication.
Our ability to work on-site with our dedicated mobile equipment is essential to our capability to provide a quality maintenance service to our customers. We are capable of providing a full team of qualified boilermakers that can work either to your plan or project manage if a plan has not been developed.
Industry/Entity Type
Industrial
Contact Information for Business Card
company name- MARLON FAB PTY LTD
story - industrial steel fabrication, constructions and pipelines
Director - Greg Hadley
workshop address - shed 7, 3862 kemble rd Tully
postal address - P.O BOX 628 TULLY Q 4854
mobile - 0429385106
w/shop phone - 0752937048
fax - 0752938159
email - admin@marlonfab.com.au
web - www.marlonfab.com.au
Logo Text
MARLON FAB pty ltd
Look and feel

```html
<!DOCTYPE html>
<html lang="en">
<head>
<meta charset="utf-8">
<title>Marlon Fab Business Card</title>
<link rel="stylesheet" href="https://fonts.googleapis.com/css2?family=Questrial&family=Arimo:wght@400;700&family=Oswald:wght@600&display=swap">
<style>
  :root {
    --stage: #e4e4e4;
    --card-white: #ffffff;
    --brand-violet: #4d4a92;
    --band-violet: #5b57a3;
    --label-lilac: #aaa4ec;
    --plate-dark: #141414;
    --plate-mid: #2a2a2c;
    --text-white: #ffffff;
    --text-black: #111111;
  }
  html, body {
    margin: 0;
    width: 1200px;
    height: 900px;
    overflow: hidden;
    background: var(--stage);
  }
  .business-card {
    position: absolute;
    left: 100px;
    top: 144px;
    width: 1000px;
    height: 612px;
    border-radius: 40px;
    overflow: hidden;
    background: var(--card-white);
    box-shadow: 0 8px 24px rgba(0,0,0,0.18);
  }
  .card-header {
    position: absolute;
    inset: 0 0 auto 0;
    height: 215px;
  }
  .brand-lockup {
    position: absolute;
    left: 48px;
    top: 30px;
    display: flex;
    align-items: flex-start;
    gap: 22px;
  }
  .brand-name {
    font-family: "Questrial", sans-serif;
    font-size: 80px;
    line-height: 76px;
    color: var(--brand-violet);
    letter-spacing: 1px;
    margin: 0;
    font-weight: 400;
  }
  .brand-square {
    width: 54px;
    height: 54px;
    background: var(--brand-violet);
    margin-top: 96px;
  }
  .contact-person {
    position: absolute;
    right: 56px;
    top: 36px;
    text-align: right;
    font-family: "Arimo", sans-serif;
  }
  .person-name {
    font-size: 27px;
    color: var(--brand-violet);
    margin: 0;
  }
  .person-role {
    font-size: 23px;
    font-weight: 700;
    color: var(--text-black);
    margin: 4px 0 0;
  }
  .tagline-band {
    position: absolute;
    left: 0;
    right: 0;
    top: 215px;
    height: 34px;
    background: var(--band-violet);
    display: flex;
    align-items: center;
    padding-left: 48px;
  }
  .tagline {
    font-family: "Oswald", sans-serif;
    font-weight: 600;
    font-size: 24px;
    letter-spacing: 2.4px;
    color: var(--text-white);
    text-transform: uppercase;
    white-space: nowrap;
  }
  .plate-area {
    position: absolute;
    left: 0;
    right: 0;
    top: 249px;
    bottom: 0;
    background: linear-gradient(160deg, var(--plate-mid) 0%, var(--plate-dark) 55%, #0b0b0b 100%);
  }
  .contact-list {
    position: absolute;
    left: 48px;
    top: 266px;
    margin: 0;
    display: grid;
    grid-template-columns: 248px auto;
    row-gap: 4px;
    font-family: "Arimo", sans-serif;
  }
  .contact-list dt {
    font-size: 29px;
    line-height: 36px;
    color: var(--label-lilac);
  }
  .contact-list dd {
    margin: 0;
    font-size: 27px;
    line-height: 36px;
    color: var(--text-white);
  }
</style>
</head>
<body>
  <article class="business-card">
    <header class="card-header">
      <div class="brand-lockup">
        <h1 class="brand-name">MARLON<br>FAB</h1>
        <div class="brand-square"></div>
      </div>
      <div class="contact-person">
        <p class="person-name">Greg Hadley</p>
        <p class="person-role">Director</p>
      </div>
    </header>

    <div class="tagline-band">
      <span class="tagline">Industrial steel fabrication, constructions and pipelines</span>
    </div>

    <div class="plate-area" role="img" aria-label="Dark diamond steel checker plate texture"></div>

    <dl class="contact-list">
      <dt>workshop address</dt><dd>- shed 7, 3862 kemble rd Tully postal</dd>
      <dt>address</dt><dd>P.O BOX 628 TULLY Q 4854</dd>
      <dt>mobile</dt><dd>0429385106</dd>
      <dt>w/shop phone</dt><dd>0752937048</dd>
      <dt>fax</dt><dd>0752938159</dd>
      <dt>email</dt><dd>admin@marlonfab.com.au</dd>
      <dt>web</dt><dd>www.marlonfab.com.au</dd>
    </dl>
  </article>
</body>
</html>
```